Blind Rivet Product catalogue

Need a design in wordpress with a productcatalogue where i present all products. This is a B2B business. The products is Blindrivets and Blindrivet nuts and accessories to this. I only want the basic information and also technical specification.

This is a subcompany to my existing company k7.m9.se but specializing in a subcategory

Target Market(s)

Businesses using blind rivet technology.

Industry/Entity Type

Industrial

Coding

Coded - Design and coding required

Number of Pages Required

5+ page

Font styles to use
Sans Serif

Requirements
Must have
• Three different categories for the products; Blind Rivets - Blind Rivet Nut - Riveting Tools
Nice to have
• Possible to ad login for more information of the different sizes

```html
<!DOCTYPE html>
<html lang="en">
<head>
<meta charset="utf-8">
<title>Open End Blind Rivet – K7M9</title>
<link href="https://fonts.googleapis.com/css2?family=Poppins:wght@300;400;500;600&display=swap" rel="stylesheet">
<style>
:root{
  --orange:#fea500;
  --navy:#154562;
  --navy-btn:#1a4463;
  --ink:#1b1b1b;
  --text:#3a3a3a;
  --panel:#f3f7fa;
  --footer:#2e3a4c;
  --footer-text:#c3c9d2;
  --line:#dfe3e7;
}
*{margin:0;padding:0;box-sizing:border-box}
html,body{width:897px;height:1200px;overflow:hidden;background:#fff}
body{font-family:'Poppins',sans-serif;color:var(--text);position:relative}
.abs{position:absolute;white-space:nowrap}

.topbar{position:absolute;left:0;top:0;width:897px;height:25px;background:var(--navy);border-top:1px solid var(--orange)}
.topbar .item{position:absolute;top:6px;font-size:7.6px;color:#fff;display:flex;align-items:center;gap:5px}
.welcome{position:absolute;left:661px;top:0;width:112px;height:24px;background:var(--orange);color:#fff;font-size:8px;font-weight:600;display:flex;align-items:center;justify-content:center}

.nav{position:absolute;left:0;top:25px;width:897px;height:33px;background:#fff}
.brand{position:absolute;left:112px;top:6px;font-size:19px;font-weight:600;color:var(--navy);letter-spacing:.5px}
.nav a{position:absolute;top:13px;font-size:7.2px;color:#333;text-decoration:none;letter-spacing:.2px}
.nav a.active{color:var(--orange);border-bottom:1px solid var(--orange);padding-bottom:2px}

.hero{position:absolute;left:0;top:58px;width:897px;height:84px;background:var(--orange);border-bottom-left-radius:112px 84px}
.crumbs{position:absolute;left:111px;top:38px;font-size:8.4px;color:#fff}
.crumbs span{margin:0 6px}
.enquiry{position:absolute;left:645px;top:23px;width:140px;height:33px;background:var(--navy-btn);color:#fff;font-size:9px;font-weight:600;display:flex;align-items:center;justify-content:center;gap:7px}

.product{position:absolute;left:112px;top:142px;width:673px;height:225px;background:var(--panel)}
.product-image{position:absolute;left:80px;top:20px;width:150px;height:200px;background:linear-gradient(135deg,#e9edf0,#c9ced3);border-radius:4px}
.product h1{position:absolute;left:336px;top:20px;font-size:17px;font-weight:400;color:var(--ink)}
.product .code{position:absolute;left:336px;top:46px;font-size:9.5px;color:var(--ink)}
.tabs{position:absolute;left:336px;top:79px;width:309px;height:22px;border-bottom:1px solid var(--line)}
.tabs div{position:absolute;top:6px;font-size:8.4px;color:#444}
.tabs div.on{color:var(--orange)}
.tabs i{position:absolute;top:0;width:1px;height:22px;background:var(--line)}
.features{position:absolute;left:342px;top:113px;list-style:none;font-size:8px;color:#333;line-height:14.5px}
.features li::before{content:"•";margin-right:3px}

.spec-kicker{position:absolute;left:0;width:897px;top:405px;text-align:center;font-size:10.6px;font-weight:500;color:#333;letter-spacing:.3px}
.spec-title{position:absolute;left:0;width:897px;top:425px;text-align:center;font-size:17.4px;font-weight:500;color:var(--ink)}
.spec-title em{font-style:normal;color:var(--orange)}
.spec-rule{position:absolute;left:434px;top:454px;width:28px;height:1px;background:var(--orange)}
.fig{position:absolute;top:479px;height:59px;background:linear-gradient(135deg,#f1f3f5,#d7dbdf);border-radius:3px}

.sizes-title{position:absolute;left:0;width:897px;top:567px;text-align:center;font-size:22px;font-weight:300;color:var(--orange)}
.sizes{position:absolute;left:0;top:601px;width:897px;height:196px;background:var(--panel)}
.sizes table{position:absolute;left:111px;top:36px;width:674px;border-collapse:collapse;font-size:8px;color:#333}
.sizes th{font-weight:500;text-align:left;font-size:8.6px;height:17px;border-bottom:1px solid var(--line);padding:0}
.sizes td{height:18px;padding:0;vertical-align:middle}
.sizes tr:nth-child(2) td{padding-top:6px;height:24px}

.cta-title{position:absolute;left:0;width:897px;top:830px;text-align:center;font-size:24.5px;font-weight:300;color:var(--orange)}
.cta-sub{position:absolute;left:0;width:897px;top:865px;text-align:center;font-size:12.8px;color:var(--orange)}
.cta-btn{position:absolute;left:406px;top:904px;width:85px;height:28px;border:1px solid var(--orange);color:var(--orange);font-size:8.4px;font-weight:500;display:flex;align-items:center;justify-content:center}

.footer{position:absolute;left:0;top:977px;width:897px;height:223px;background:var(--footer);border-top:3px solid var(--orange);border-top-right-radius:95px 70px}
.footer h3{position:absolute;font-size:11.6px;font-weight:500;color:#fff;top:36px}
.footer .t{position:absolute;font-size:8.2px;color:var(--footer-text);display:flex;align-items:center}
.footer .dot{width:4px;height:4px;border:1px solid var(--orange);border-radius:50%;margin-right:6px}
.social{position:absolute;top:67px;width:11px;height:11px;border-radius:2px;background:#fff}
.footer .divider{position:absolute;left:123px;top:178px;width:651px;height:1px;background:rgba(255,255,255,.12)}
.totop{position:absolute;left:437px;top:171px;width:23px;height:13px;background:var(--orange);border-radius:2px;display:flex;align-items:center;justify-content:center}
.copy{position:absolute;left:0;width:897px;top:195px;text-align:center;font-size:7.8px;color:var(--footer-text)}
</style>
</head>
<body>

<header class="topbar">
  <div class="item" style="left:112px">
    <svg width="7" height="7" viewBox="0 0 24 24"><path fill="#fea500" d="M6.6 10.8a15 15 0 0 0 6.6 6.6l2.2-2.2c.3-.3.7-.4 1-.2 1.1.4 2.3.6 3.6.6.6 0 1 .4 1 1V20c0 .6-.4 1-1 1A17 17 0 0 1 3 4c0-.6.4-1 1-1h3.5c.6 0 1 .4 1 1 0 1.3.2 2.5.6 3.6.1.3 0 .7-.2 1z"/></svg>
    0123 - 45 67 89
  </div>
  <div class="item" style="left:202px">
    <svg width="8" height="6" viewBox="0 0 24 18"><rect width="24" height="18" rx="2" fill="#fea500"/><path d="M1 2l11 8 11-8" stroke="#154562" stroke-width="2" fill="none"/></svg>
    erik@k7.m9.se
  </div>
  <div class="welcome">Welcome To Lena Berg</div>
</header>

<nav class="nav">
  <div class="brand">K7M9</div>
  <a style="left:516px">HOME</a>
  <a style="left:555px">ABOUT US</a>
  <a class="active" style="left:610px">PRODUCTS</a>
  <svg class="abs" style="left:652px;top:15px" width="5" height="3" viewBox="0 0 10 6"><path d="M0 0h10L5 6z" fill="#333"/></svg>
  <a style="left:668px">CONTACT US</a>
  <a style="left:731px">|</a>
  <svg class="abs" style="left:748px;top:10px" width="13" height="13" viewBox="0 0 26 26"><circle cx="13" cy="13" r="12.5" fill="#f4f4f4"/><circle cx="12" cy="12" r="4" stroke="#333" stroke-width="1.8" fill="none"/><path d="M15 15l3.5 3.5" stroke="#333" stroke-width="1.8"/></svg>
  <svg class="abs" style="left:771px;top:10px" width="14" height="14" viewBox="0 0 28 28"><clipPath id="fc"><circle cx="14" cy="14" r="14"/></clipPath><g clip-path="url(#fc)"><rect width="28" height="28" fill="#1f5fa8"/><rect x="8" width="4" height="28" fill="#fecc00"/><rect y="12" width="28" height="4" fill="#fecc00"/></g></svg>
</nav>

<section class="hero">
  <div class="crumbs">Products<span>|</span>Blind Rivets<span>|</span>Open end Blind Rivets</div>
  <div class="enquiry">
    <svg width="14" height="12" viewBox="0 0 28 24"><path d="M2 2h24v15H10l-6 5v-5H2z" stroke="#fff" stroke-width="1.6" fill="none"/></svg>
    Product Enquiry
  </div>
</section>

<section class="product">
  <div class="product-image" role="img" aria-label="Photo of an open end blind rivet"></div>
  <h1>Open End Blind Rivet</h1>
  <div class="code">DIN 7337 A2 3.2X10</div>
  <div class="tabs">
    <div class="on" style="left:18px">Features</div>
    <i style="left:78px"></i>
    <div style="left:90px">Application</div>
    <i style="left:157px"></i>
    <div style="left:173px">Materials</div>
  </div>
  <ul class="features">
    <li>Lorem ipsum dolor sit amet, consectetur adipiscing elit.</li>
    <li>Sed a mauris a sem vehicula commodo.</li>
    <li>Etiam a justo a turpis pellentesque viverra.</li>
    <li>Vestibulum ultrices velit sit amet massa tristique malesuada.</li>
  </ul>
</section>

<div class="spec-kicker">Technical Specification</div>
<div class="spec-title">Open End <em>Blind Rivet</em></div>
<div class="spec-rule"></div>
<div class="fig" style="left:305px;width:90px" role="img" aria-label="Side view of the blind rivet"></div>
<div class="fig" style="left:415px;width:126px" role="img" aria-label="Dimensioned technical drawing of the rivet"></div>
<div class="fig" style="left:552px;width:43px" role="img" aria-label="Section drawing of the set rivet"></div>

<div class="sizes-title">Sizes</div>
<section class="sizes">
  <table>
    <tr><th style="width:152px">Diameter (D)</th><th style="width:202px">Length (L)</th><th>Grip Range</th></tr>
    <tr><td>3.2</td><td>6.0 (1/4")</td><td>0.5 - 3.0 (0.02 - 0.12")</td></tr>
    <tr><td></td><td>8.0 (5/16")</td><td>3.0 - 5.0 (0.12 - 0.20")</td></tr>
    <tr><td></td><td>10.0 (3/8")</td><td>5.0 - 7.0 (0.20 - 0.28")</td></tr>
    <tr><td></td><td>12.0 (15/32")</td><td>7.0 - 9.0 (0.28 - 0.35")</td></tr>
    <tr><td></td><td>14.0 (9/16")</td><td>9.0 - 11.0 (0.35 - 0.43")</td></tr>
    <tr><td></td><td>16.0 (5/8")</td><td>11.0 - 13.0 (0.43 - 0.51")</td></tr>
  </table>
</section>

<div class="cta-title">Need help choosing the right blind rivets?</div>
<div class="cta-sub">Talk to one of our representative who can help</div>
<div class="cta-btn">Contact Us</div>

<footer class="footer">
  <h3 style="left:140px">Quick Contact</h3>
  <svg class="abs" style="left:140px;top:57px" width="7" height="10" viewBox="0 0 14 20"><path d="M7 0a7 7 0 0 0-7 7c0 5 7 13 7 13s7-8 7-13a7 7 0 0 0-7-7z" fill="#fea500"/><circle cx="7" cy="7" r="2.5" fill="#2e3a4c"/></svg>
  <div class="t" style="left:157px;top:55px">k7.m9.se</div>
  <div class="t" style="left:157px;top:69px">14B Harbour street</div>
  <div class="t" style="left:157px;top:83px">Co. Lorem Ipsum</div>
  <svg class="abs" style="left:140px;top:107px" width="9" height="9" viewBox="0 0 24 24"><path fill="#fea500" d="M6.6 10.8a15 15 0 0 0 6.6 6.6l2.2-2.2c.3-.3.7-.4 1-.2 1.1.4 2.3.6 3.6.6.6 0 1 .4 1 1V20c0 .6-.4 1-1 1A17 17 0 0 1 3 4c0-.6.4-1 1-1h3.5c.6 0 1 .4 1 1 0 1.3.2 2.5.6 3.6.1.3 0 .7-.2 1z"/></svg>
  <div class="t" style="left:157px;top:105px">0123 - 45 67 89</div>
  <svg class="abs" style="left:140px;top:130px" width="9" height="7" viewBox="0 0 24 18"><rect width="24" height="18" rx="2" fill="#fea500"/><path d="M1 2l11 8 11-8" stroke="#2e3a4c" stroke-width="2" fill="none"/></svg>
  <div class="t" style="left:157px;top:127px">erik@k7.m9.se</div>

  <h3 style="left:415px">Quick Links</h3>
  <div class="t" style="left:415px;top:54px"><span class="dot"></span>Home</div>
  <div class="t" style="left:415px;top:72px"><span class="dot"></span>About Us</div>
  <div class="t" style="left:415px;top:90px"><span class="dot"></span>Products</div>
  <div class="t" style="left:415px;top:108px"><span class="dot"></span>Contact Us</div>

  <h3 style="left:624px">Our Social Media!</h3>
  <div class="t" style="left:624px;top:53px;color:#98a2ae">Follow and get to know us!</div>
  <div class="social" style="left:625px"></div>
  <div class="social" style="left:645px"></div>
  <div class="social" style="left:666px"></div>
  <div class="social" style="left:686px"></div>

  <div class="divider"></div>
  <div class="totop"><svg width="10" height="6" viewBox="0 0 20 12"><path d="M2 10l8-7 8 7" stroke="#2e3a4c" stroke-width="3" fill="none"/></svg></div>
  <div class="copy">© Copyright 2020. k7.m9.se. All rights reserved</div>
</footer>

</body>
</html>
```